Independence Day Graphics for Sale

I want to create 10 social media graphics (new Pictora size 4:5 (1080 x 1350 pixels) focusing on our July 4th Sale Graphics, using any of the pics attached. Use the attached pics, NO RANDOM STOCK PHOTOGRAPHY. For the color scheme of the graphics, they should all be complementary to the product colors in the photos.
You can add any of the photos attached but none are required. You can do some of the graphics in all text. I mainly need BOLD text that says one of the headlines (10 total) SEE ATTACHED WORD DOCUMENT for the headlines to use.

Target Market(s)

women looking to lose weight

Requirements
Must have
• pics attached and text attached

```html
<!DOCTYPE html>
<html lang="en">
<head>
<meta charset="utf-8">
<title>July 4th Sale Social Graphics</title>
<link href="https://fonts.googleapis.com/css2?family=Anton&display=swap" rel="stylesheet">
<style>
:root{
  --sheet:#d0d0d0;
  --purple:#3b2c78;
  --purple-deep:#33256b;
  --glow:#2d4fb3;
  --red:#ec1a22;
  --white:#ffffff;
  --bottle:#ecebef;
  --bottle-shade:#c9c6d3;
  --room:#8a6a55;
  --counter:#e9e6ea;
}
*{margin:0;padding:0;box-sizing:border-box}
html,body{width:1200px;height:611px;overflow:hidden;background:var(--sheet)}
.sheet{position:relative;width:1200px;height:611px}
.tile{position:absolute;width:224px;height:280px;overflow:hidden;
  background:radial-gradient(ellipse 75% 55% at 45% 55%,var(--glow) 0%,var(--purple) 70%,var(--purple-deep) 100%);
  font-family:'Anton',Impact,sans-serif;text-transform:uppercase}
.row1{top:21px}.row2{top:312px}
.c1{left:19px}.c2{left:254px}.c3{left:489px}.c4{left:723px}.c5{left:958px}
.copy{position:absolute;left:0;right:0;text-align:center;line-height:.92}
.copy p{white-space:nowrap}
.red{color:var(--red);-webkit-text-stroke:.6px var(--white)}
.white{color:var(--white)}
.mixed{text-transform:none;text-align:left;left:17px}
.bottles{position:absolute;left:20px;right:20px;bottom:14px;height:74px;border-radius:6px;
  background:linear-gradient(180deg,var(--bottle) 0%,var(--bottle-shade) 100%);opacity:.92}
.scene .photo{position:absolute;top:0;right:0;width:55%;height:100%;
  background:linear-gradient(180deg,var(--room) 0%,#6c5a6e 45%,var(--purple) 100%)}
.scene .counter{position:absolute;left:0;right:0;bottom:0;height:62px;
  background:linear-gradient(90deg,var(--purple) 0%,var(--purple) 30%,var(--counter) 100%);opacity:.85}
.scene .bottles{left:18px;right:auto;width:120px;bottom:18px;height:60px}
.inline-bottles{display:inline-block;width:88px;height:44px;border-radius:4px;vertical-align:middle;
  background:linear-gradient(180deg,var(--bottle),var(--bottle-shade));margin-right:6px}
</style>
</head>
<body>
<main class="sheet">

  <section class="tile row1 c1">
    <div class="copy" style="top:18px">
      <p class="red" style="font-size:46px">July 4th</p>
      <p class="white" style="font-size:35px">Mega Sale!</p>
      <p class="red" style="font-size:43px">25% Off</p>
      <p class="white" style="font-size:37px">Everything</p>
    </div>
    <div class="bottles" role="img" aria-label="Row of four supplement bottles"></div>
  </section>

  <section class="tile row1 c2 scene">
    <div class="photo" role="img" aria-label="Smiling woman in a white crop top holding a supplement bottle"></div>
    <div class="counter" role="img" aria-label="Supplement bottles on a marble counter"></div>
    <div class="bottles" role="img" aria-label="Group of supplement bottles"></div>
    <div class="copy mixed" style="top:20px">
      <p class="red" style="font-size:29px">Biggest</p>
      <p class="red" style="font-size:29px">4th of July</p>
      <p class="red" style="font-size:29px">Sale Ever!</p>
      <p class="white" style="font-size:29px">25% OFF</p>
      <p class="white" style="font-size:29px">Sitewide</p>
    </div>
  </section>

  <section class="tile row1 c3 scene">
    <div class="photo" role="img" aria-label="Smiling woman in a white crop top holding a supplement bottle"></div>
    <div class="counter" role="img" aria-label="Supplement bottles on a marble counter"></div>
    <div class="bottles" role="img" aria-label="Group of supplement bottles"></div>
    <div class="copy mixed" style="top:20px;left:17px">
      <p class="white" style="font-size:34px">Mega</p>
      <p class="white" style="font-size:34px">Summer</p>
      <p class="white" style="font-size:34px">Blowout!</p>
      <p class="red" style="font-size:29px">25% OFF</p>
      <p class="red" style="font-size:29px">Everything</p>
    </div>
  </section>

  <section class="tile row1 c4 scene">
    <div class="photo" role="img" aria-label="Smiling woman in a white crop top standing behind supplements"></div>
    <div class="counter" role="img" aria-label="Supplement bottles on a marble counter"></div>
    <div class="bottles" role="img" aria-label="Group of supplement bottles"></div>
    <div class="copy mixed" style="top:20px">
      <p class="white" style="font-size:31px">Historic</p>
      <p class="white" style="font-size:31px">4th of July</p>
      <p class="white" style="font-size:31px">Sale Ever!</p>
      <p class="red" style="font-size:31px">25% OFF</p>
      <p class="red" style="font-size:31px">Sitewide</p>
    </div>
  </section>

  <section class="tile row1 c5 scene">
    <div class="photo" role="img" aria-label="Smiling woman in a white crop top standing behind supplements"></div>
    <div class="counter" role="img" aria-label="Supplement bottles on a marble counter"></div>
    <div class="bottles" role="img" aria-label="Group of supplement bottles"></div>
    <div class="copy mixed" style="top:24px">
      <p class="white" style="font-size:23px">Last Chance</p>
      <p class="red" style="font-size:32px">25% Off</p>
      <p class="white" style="font-size:40px">Time Is</p>
      <p class="red" style="font-size:23px">Running Out!</p>
    </div>
  </section>

  <section class="tile row2 c1">
    <div class="copy" style="top:16px">
      <p class="red" style="font-size:48px">One-Time</p>
      <p class="white" style="font-size:40px"><span class="inline-bottles" role="img" aria-label="Small group of supplement bottles"></span>Only</p>
      <p class="red" style="font-size:48px">25% Off</p>
      <p class="white" style="font-size:30px">Of Everything!</p>
    </div>
    <div class="bottles" role="img" aria-label="Row of four supplement bottles"></div>
  </section>

  <section class="tile row2 c2">
    <div class="copy" style="top:24px">
      <p class="white" style="font-size:44px">25% Off</p>
      <p class="red" style="font-size:29px">Stock-Up Event</p>
      <p class="white" style="font-size:44px">25% Off</p>
      <p class="red" style="font-size:26px">All Supplements</p>
    </div>
    <div class="bottles" role="img" aria-label="Row of four supplement bottles"></div>
  </section>

  <section class="tile row2 c3">
    <div class="copy" style="top:26px">
      <p class="white" style="font-size:38px">The Lowest</p>
      <p class="red" style="font-size:25px">Prices We've Ever</p>
      <p class="white" style="font-size:50px">Offered!</p>
      <p class="red" style="font-size:46px">25% Off</p>
      <p class="white" style="font-size:41px">Everything</p>
    </div>
  </section>

  <section class="tile row2 c4">
    <div class="copy" style="top:24px">
      <p class="white" style="font-size:36px">Our Biggest</p>
      <p class="red" style="font-size:30px">Discount Ever!</p>
      <p class="white" style="font-size:46px">25% Off</p>
      <p class="red" style="font-size:40px">Everything</p>
    </div>
    <div class="bottles" role="img" aria-label="Row of four supplement bottles"></div>
  </section>

  <section class="tile row2 c5">
    <div class="copy" style="top:38px">
      <p class="white" style="font-size:40px">Don't Wait!</p>
      <p class="red" style="font-size:48px">25% Off</p>
      <p class="white" style="font-size:44px">Ends Soon</p>
    </div>
    <div class="bottles" role="img" aria-label="Row of four supplement bottles"></div>
  </section>

</main>
</body>
</html>
```